Invoice ... please do not write invoice or INVOICE on it !!!

look the Old PDF , I want a new invoice with the logo you created .

it should be only 256 KB pdf size file.
I should be a PDF file.

on top

Practice for Osteopathy & Naturopathy

the my name etc.

Look at www.koerperpraxis-velmsdorf.de

there's cooler s you can include in the invoice

I send you 2 LOGOS, these logos have to included in the INVOICE.

```html
<!DOCTYPE html>
<html lang="de">
<head>
<meta charset="utf-8">
<title>Praxis für Osteopathie &amp; Naturheilkunde – Leistungsrechnung</title>
<link href="https://fonts.googleapis.com/css2?family=Josefin+Sans:wght@300;400;600&display=swap" rel="stylesheet">
<style>
  :root{
    --backdrop:#140a33;
    --paper:#ffffff;
    --header-grey:#efefef;
    --navy:#253b6e;
    --navy-text:#1f2f63;
    --gold:#9a7a3a;
    --gold-light:#dcc064;
    --gold-dark:#8a6c2e;
  }
  *{margin:0;padding:0;box-sizing:border-box}
  html,body{width:1200px;height:1200px;overflow:hidden;background:var(--backdrop);font-family:"Josefin Sans",sans-serif}
  .sheet{position:absolute;left:206px;top:42px;width:788px;height:1115px;background:var(--paper);overflow:hidden}
  .sheet-header{position:absolute;left:0;top:0;width:100%;height:194px;background:var(--header-grey)}
  .brand{position:absolute;left:18px;top:18px;width:320px;text-align:center}
  .brand-circle{width:104px;height:104px;border-radius:50%;border:3px solid var(--navy);margin:0 auto 12px}
  .brand-name{font-size:21px;font-weight:600;letter-spacing:1.5px;text-transform:uppercase;color:var(--navy)}
  .contact{position:absolute;left:540px;top:18px;list-style:none;color:var(--gold);font-weight:300;font-size:17px}
  .contact li{display:flex;align-items:flex-start;height:33px}
  .contact li.address{height:64px}
  .contact svg{width:22px;height:22px;margin-right:11px;flex:none;margin-top:-3px}
  .contact .lines{line-height:30px;margin-top:-6px}
  .gold-stripe{position:absolute;left:0;top:194px;width:100%;height:9px;background:linear-gradient(90deg,var(--gold-dark),var(--gold-light) 50%,var(--gold-dark))}
  .title-band{position:absolute;left:0;top:203px;width:100%;height:53px;background:var(--navy);color:#fff;font-size:38px;font-weight:400;text-align:center;line-height:60px;letter-spacing:.5px}
  .practitioner{position:absolute;left:0;top:266px;width:100%;text-align:center;color:var(--navy-text);font-size:26px}
  .roles{position:absolute;left:205px;top:308px;width:386px;height:27px;border-radius:14px;background:linear-gradient(90deg,var(--gold-dark),#b99a4c 50%,var(--gold-dark));color:#fff;font-size:19px;text-align:center;line-height:31px;font-weight:300}
  .practice-address{position:absolute;left:0;top:349px;width:100%;text-align:center;color:var(--navy-text);font-size:17px}
  .invoice-table{position:absolute;left:94px;top:435px;width:603px;border-collapse:collapse;color:var(--navy-text);font-size:19px;font-weight:300}
  .invoice-table td{border:1.5px solid var(--gold);padding:6px 19px 0;vertical-align:middle}
  .invoice-table td.label{width:249px}
  .footer-rule-blue{position:absolute;left:0;top:942px;width:261px;height:5px;background:var(--navy);border-radius:0 3px 3px 0}
  .footer-rule-gold{position:absolute;left:267px;top:942px;width:521px;height:5px;background:var(--gold);border-radius:3px 0 0 3px}
  .badge{position:absolute;background:#e6e6e6}
  .badge-round{left:22px;top:967px;width:112px;height:112px;border-radius:50%;border:3px solid #2a2a2a;background:#f3f3f3}
  .badge-square{left:143px;top:968px;width:106px;height:106px;background:#ececec}
  .bank{position:absolute;left:289px;top:972px;width:473px;color:var(--navy-text)}
  .bank-heading{font-size:18px;font-weight:600;color:var(--gold);padding-bottom:7px;border-bottom:1.5px solid var(--gold)}
  .bank-holder{font-size:19px;margin-top:12px}
  .bank-row{display:flex;justify-content:space-between;font-size:17px;margin-top:14px;font-weight:300}
  .bank-row b{font-weight:600}
  .footer-band{position:absolute;left:0;top:1093px;width:100%;height:22px;background:var(--navy)}
</style>
</head>
<body>
<div class="sheet">
  <header class="sheet-header">
    <div class="brand">
      <div class="brand-circle"></div>
      <div class="brand-name">Osteopathie Velmsdorf</div>
    </div>
    <ul class="contact">
      <li class="address">
        <svg viewBox="0 0 24 24" fill="none" stroke="#253b6e" stroke-width="1.3"><circle cx="12" cy="12" r="11"/><circle cx="12" cy="10" r="3"/><path d="M7 17c1-2 3-3 5-3s4 1 5 3"/></svg>
        <div class="lines">Lindenhofweg 12<br>48213 Velmsdorf</div>
      </li>
      <li>
        <svg viewBox="0 0 24 24" fill="none" stroke="#253b6e" stroke-width="1.3"><circle cx="12" cy="12" r="11"/><path d="M8 7l2 0 1 3-1.5 1c.8 1.6 1.9 2.7 3.5 3.5l1-1.5 3 1v2c-5 0-9-4-9-9z"/></svg>
        <span>0563 / 4418207</span>
      </li>
      <li>
        <svg viewBox="0 0 24 24" fill="none" stroke="#253b6e" stroke-width="1.3"><circle cx="12" cy="12" r="11"/><circle cx="12" cy="12" r="6"/><path d="M6 12h12M12 6c-2 2-2 10 0 12M12 6c2 2 2 10 0 12"/></svg>
        <span>www.koerperpraxis-velmsdorf.de</span>
      </li>
      <li>
        <svg viewBox="0 0 24 24" fill="none" stroke="#253b6e" stroke-width="1.3"><circle cx="12" cy="12" r="11"/><rect x="6.5" y="8" width="11" height="8"/><path d="M6.5 8l5.5 5 5.5-5M6.5 16l4-4M17.5 16l-4-4"/></svg>
        <span>info@koerperpraxis-velmsdorf.de</span>
      </li>
    </ul>
  </header>
  <div class="gold-stripe"></div>
  <h1 class="title-band">Praxis für Osteopathie &amp; Naturheilkunde</h1>

  <h2 class="practitioner" style="font-weight:400">Jonas Brenner</h2>
  <div class="roles">Osteopath - Heilpraktiker - Physiotherapeut</div>
  <p class="practice-address">Praxis Brenner, Lindenhofweg 12 , 48213 Velmsdorf</p>

  <table class="invoice-table">
    <tr style="height:56px"><td class="label">Name:</td><td></td></tr>
    <tr style="height:58px"><td class="label">Leistungsrechnung Nr.:</td><td>504/21</td></tr>
    <tr style="height:57px"><td class="label">Rech Datum:</td><td>2/1/2021</td></tr>
    <tr style="height:54px"><td class="label">privat/gesetzl.&nbsp;&nbsp; p od. g p:</td><td>0</td></tr>
    <tr style="height:53px"><td class="label">erwachsen/kind e od. k e:</td><td>0</td></tr>
    <tr style="height:52px"><td class="label">Diagnose:</td><td>Osteopathische Dysfunktionen</td></tr>
    <tr style="height:53px"><td class="label">weitere Diagnosen:</td><td>BWS-Blockade</td></tr>
    <tr style="height:52px"><td class="label">weitere Diagnosen:</td><td>??</td></tr>
  </table>

  <div class="footer-rule-blue"></div>
  <div class="footer-rule-gold"></div>
  <div class="badge badge-round" role="img" aria-label="Mitgliedsabzeichen Osteopathenverband"></div>
  <div class="badge badge-square" role="img" aria-label="Mitgliedsabzeichen Heilpraktikerverband"></div>

  <section class="bank">
    <div class="bank-heading">Bankverbindung:</div>
    <div class="bank-holder">Jonas Brenner</div>
    <div class="bank-row">
      <span><b>IBAN:</b> DE00 1234 5678 9012 3456 78</span>
      <span><b>BIC:</b> ABCDDEFFXXX</span>
    </div>
  </section>
  <div class="footer-band"></div>
</div>
</body>
</html>
```